Collectible Fun Cards for Children

I have an idea of the type of card we want. Looking for an illustrator to help bring the idea to life very quickly. The cards will be in three series, with each series having a total of 36 cards each. I can supply most of the ideas for the cards but will need the successful designer to craft the cards in an attractive way. Ideally each car card will be of a different color. The preference will be for the two card images supplied to be merged. Of course, the successful candidate will be the one who is able to make come up with the best design, even better than the ones supplied.
I have added a hand-designed rendition of the card I have in mind for guidance.
The Purpose
• Engagement: Make kids excited to collect, trade, and read them.
• Education: Slip in simple but accurate nutrition, growth, and development facts.
• Branding: Position our brand as a premium, fun, and trustworthy product.

Target Market(s)

Children

Industry/Entity Type

Health and Wellness

Requirements
Must have
• Fun characters
Should not have
• Profanity. Incorrect information

```html
<!DOCTYPE html>
<html lang="en">
<head>
<meta charset="utf-8">
<title>VitaKids Nutrition Hero Card</title>
<link rel="stylesheet" href="https://fonts.googleapis.com/css2?family=League+Spartan:wght@700&family=Fredoka:wght@600;700&family=Cabin:wght@500&family=Nunito:wght@800&display=swap">
<style>
  :root {
    --page: #ffffff;
    --card-border: #e86e3a;
    --orange-light: #f39c47;
    --orange-deep: #e86e3a;
    --sun-yellow: #fbe04a;
    --hero-red: #d63a2b;
    --badge-red: #c01f2f;
    --ink: #111111;
    --white: #ffffff;
    --cape-purple: #4a2f80;
  }
  * { margin: 0; padding: 0; box-sizing: border-box; }
  html, body {
    width: 849px; height: 1200px; overflow: hidden;
    background: var(--page);
  }
  .canvas { position: relative; width: 849px; height: 1200px; }
  .hero-card {
    position: absolute; left: 121px; top: 171px;
    width: 582px; height: 872px;
    border: 4px solid var(--card-border);
    border-radius: 22px;
    overflow: hidden;
    background: var(--sun-yellow);
  }
  .brand-strip {
    height: 59px; background: var(--orange-light);
    display: flex; align-items: center; justify-content: center;
  }
  .brand-name {
    font-family: "Fredoka", sans-serif; font-weight: 600;
    font-size: 31px; color: var(--white);
    padding-top: 6px;
  }
  .title-band {
    height: 165px; background: var(--orange-deep);
    display: flex; flex-direction: column; align-items: center; justify-content: center;
    padding-top: 10px;
  }
  .hero-title {
    font-family: "League Spartan", sans-serif; font-weight: 700;
    color: var(--white); font-size: 64px; line-height: 64px;
    text-align: center;
  }
  .art-panel {
    height: 374px; background: var(--orange-light);
  }
  .hero-art {
    position: absolute; left: 143px; top: 209px;
    width: 357px; height: 376px;
    border-radius: 48% 48% 44% 44%;
    background: radial-gradient(circle at 48% 48%, var(--sun-yellow) 0%, #f7c23f 38%, var(--orange-deep) 64%, rgba(74,47,128,0.55) 85%, rgba(243,156,71,0) 100%);
  }
  .fact-panel {
    text-align: center; padding-top: 10px;
  }
  .fact-heading {
    font-family: "Fredoka", sans-serif; font-weight: 700;
    font-size: 54px; line-height: 58px; color: var(--hero-red);
  }
  .fact-text {
    margin-top: 8px;
    font-family: "Cabin", sans-serif; font-weight: 500;
    font-size: 24px; line-height: 27px; color: var(--ink);
  }
  .series-badge {
    position: absolute; left: 121px; top: 784px;
    width: 331px; height: 47px; border-radius: 24px;
    background: var(--badge-red);
    display: flex; align-items: center; justify-content: center;
    font-family: "Nunito", sans-serif; font-weight: 800;
    font-size: 24px; letter-spacing: 2px; color: var(--white);
    word-spacing: 6px;
  }
</style>
</head>
<body>
<div class="canvas">
  <article class="hero-card">
    <header class="brand-strip">
      <span class="brand-name">VitaKids</span>
    </header>
    <section class="title-band">
      <h1 class="hero-title">VITAMIN C<br>CARROT</h1>
    </section>
    <section class="art-panel"></section>
    <div class="hero-art" role="img" aria-label="Carrot superhero character in purple mask and cape, waving, with a yellow starburst and lightning bolts behind"></div>
    <section class="fact-panel">
      <h2 class="fact-heading">Did you Know?</h2>
      <p class="fact-text">VITAMIN C helps your body<br>heal cuts and fight germs- like<br>A superhero!!</p>
    </section>
    <div class="series-badge">NUTRITION HERO &nbsp;1</div>
  </article>
</div>
</body>
</html>
```